Bath Salt - Sachet Packet (5 Scents) Packaging Design

We sell products to professional salons in the USA. This product is used as the first step when treating clients to a pedicure spa. This product is called SALT SOAK (or Bath Salts). The salt is added to the water to cleanse the skin, create a pleasant fragrance, and change the color of the water.

This product has 5 different variations, based on the scent of the salt soak. The available scents are:
LAVENDER, MANDARIN, CUCUMBER-MELON, JASMINE, MINT.

We would like to see package designs for all 5 scents. The theme should be consistent across the different variations of scents. The design should focus on bright, attractive, floral colors/themes. The design should fully express the color and imagery that are associated with each scent. (Lavender scent should include purple colors, lavender flower, etc.). See example images for reference of popular designs/brands.

Ideal designs will incorporate a luxurious and premium aesthetic that combines elegant imagery, colors, and premium finishes. See example images for reference of popular designs/brands.

Each packet is individually sealed. See dimension artwork file for reference of the sachet packet size and layout.

See the attached document guidelines for more information about product name, key text, and brand logo.

Target Market(s)

Beauty & Nail Salons

Industry/Entity Type

Beauty

Font styles to use
Sans Serif
Script

Requirements
Must have
• Bright imagery and colors that relate to the target fragrance
Nice to have
• Premium and luxurious finishes (shiny accent, etc.)

```html
<!DOCTYPE html>
<html lang="en">
<head>
<meta charset="utf-8">
<title>Sea Salt Soak Sachets – Orla</title>
<link href="https://fonts.googleapis.com/css2?family=Montserrat:wght@800&family=Quicksand:wght@400;500&display=swap" rel="stylesheet">
<style>
  :root{
    --backdrop:#ececed;
    --melon-deep:#1f5a22;
    --melon-mid:#3f8a3a;
    --melon-light:#8fc07a;
    --lavender-deep:#6a3f9e;
    --lavender-mid:#9b6fcc;
    --lavender-light:#d4c2ee;
    --label-white:rgba(255,255,255,0.82);
    --band-white:rgba(255,255,255,0.78);
    --title-purple:#5b2d91;
    --body-grey:#4d4d55;
    --dot-white:#ffffff;
  }
  *{box-sizing:border-box;margin:0;padding:0}
  html,body{width:1200px;height:1200px;overflow:hidden}
  body{background:var(--backdrop);position:relative;font-family:"Quicksand",sans-serif}

  .sachet{position:absolute;overflow:hidden;box-shadow:0 18px 40px rgba(0,0,0,0.18)}
  .sachet--cucumber{left:107px;top:287px;width:473px;height:791px}
  .sachet--lavender{left:635px;top:412px;width:435px;height:632px}

  .sachet__artwork{position:absolute;inset:0}
  .sachet--cucumber .sachet__artwork{
    background:linear-gradient(160deg,var(--melon-mid) 0%,var(--melon-deep) 35%,var(--melon-light) 60%,var(--melon-deep) 100%);
  }
  .sachet--lavender .sachet__artwork{
    background:linear-gradient(160deg,var(--lavender-light) 0%,var(--lavender-mid) 40%,var(--lavender-deep) 70%,var(--lavender-mid) 100%);
  }

  .sachet__border{position:absolute;inset:0;width:100%;height:100%}

  .name-label{position:absolute;background:var(--label-white);text-align:center}
  .sachet--cucumber .name-label{left:87px;top:100px;width:300px;height:76px}
  .sachet--lavender .name-label{left:79px;top:0;width:270px;height:145px}
  .name-label__arc{display:block;width:100%;height:52px}
  .sachet--lavender .name-label__arc{margin-top:62px}
  .name-label__arc text{font-family:"Montserrat",sans-serif;font-weight:800;font-size:25px;fill:var(--title-purple)}
  .name-label__scent{font-family:"Quicksand",sans-serif;font-weight:400;font-size:17px;letter-spacing:0.5px;color:var(--body-grey);text-transform:uppercase;margin-top:-10px}

  .brand-band{position:absolute;left:0;right:0;background:var(--band-white);display:flex;align-items:center;justify-content:center}
  .sachet--cucumber .brand-band{top:267px;height:173px}
  .sachet--lavender .brand-band{top:231px;height:184px}
  .brand-band__name{font-family:"Quicksand",sans-serif;font-weight:500;font-size:84px;line-height:1;color:var(--body-grey)}

  .claim-label{position:absolute;background:var(--label-white);display:flex;align-items:center;justify-content:center;font-size:21px;font-weight:500;color:var(--body-grey)}
  .sachet--cucumber .claim-label{left:87px;top:587px;width:293px;height:69px}
  .sachet--lavender .claim-label{left:79px;top:529px;width:270px;height:72px}
</style>
</head>
<body>

<section class="sachet sachet--cucumber">
  <div class="sachet__artwork" role="img" aria-label="Close-up of cucumber and melon rind on a green foil surface"></div>
  <svg class="sachet__border" viewBox="0 0 473 791" aria-hidden="true">
    <rect x="22" y="57" width="429" height="712" fill="none" stroke="var(--dot-white)" stroke-width="7" stroke-linecap="round" stroke-dasharray="0 11"/>
  </svg>
  <div class="name-label">
    <svg class="name-label__arc" viewBox="0 0 300 52">
      <path id="arc-cucumber" d="M30,46 Q150,8 270,46" fill="none"/>
      <text text-anchor="middle"><textPath href="#arc-cucumber" startOffset="50%">SEA SALT SOAK</textPath></text>
    </svg>
    <p class="name-label__scent">Cucumber-Melon</p>
  </div>
  <div class="brand-band">
    <p class="brand-band__name">Orla</p>
  </div>
  <p class="claim-label">Organic Ingredients</p>
</section>

<section class="sachet sachet--lavender">
  <div class="sachet__artwork" role="img" aria-label="Field of purple lavender blossoms"></div>
  <svg class="sachet__border" viewBox="0 0 435 632" aria-hidden="true">
    <rect x="18" y="36" width="399" height="566" fill="none" stroke="var(--dot-white)" stroke-width="7" stroke-linecap="round" stroke-dasharray="0 11"/>
  </svg>
  <div class="name-label">
    <svg class="name-label__arc" viewBox="0 0 270 52">
      <path id="arc-lavender" d="M20,48 Q135,8 250,48" fill="none"/>
      <text text-anchor="middle"><textPath href="#arc-lavender" startOffset="50%">SEA SALT SOAK</textPath></text>
    </svg>
    <p class="name-label__scent">Lavender</p>
  </div>
  <div class="brand-band">
    <p class="brand-band__name">Orla</p>
  </div>
  <p class="claim-label">Organic Ingredients</p>
</section>

</body>
</html>
```